Natural and organic skincare brand needs label design!

I need labels designed for my natural and organic skincare brand velmurine. The front of the bottles must contain the logo (image attached) and the following words: Formulated by a Naturopath; Anti-aging therapy; Organic Facial Oil; with CoEnzyme Q10 and Rosehip Seed Oil; 100ml e3.38fl.oz. Colours I would like used include black/white/grey/silver and aqua. I also like the grey woodgrain used on my draft website (check out www.velmurine.com.au). The logo should be silver foil (shiny).The final design should be simple and communicate nature and sophistication. Some designs I like are found in the attachments. I intend to use black or white bottles.

women aged 30-50 interested in natural products

Skin Care Product

Serif
Sans Serif
Decorative
Script
• Any

• Dimensions: 62mm (w) x 75mm (H) (front label only)
• Must contain the logo (image attached). The logo should be silver foil (shiny). and the following words are to be included on the label:
• Formulated by a Naturopath;
• Anti-aging Therapy;
• Organic Facial Oil;
• with CoEnzyme Q10 and Rosehip Seed Oil;
• 100ml e3.38fl.oz.
• Colours I would like used include black/white/grey/silver and aqua (turquoise). But I am also open to suggestion. I also like the grey woodgrain used on my draft website (check out www.velmurine.com.au)

```html
<!DOCTYPE html>
<html lang="en">
<head>
<meta charset="utf-8">
<title>velmurine – Anti-aging Therapy label</title>
<link href="https://fonts.googleapis.com/css2?family=Dancing+Script:wght@500&family=PT+Sans:wght@400&family=Tinos:ital,wght@0,400;1,700&display=swap" rel="stylesheet">
<style>
  :root {
    --page-bg: #f3f3f3;
    --label-border: #ffffff;
    --aqua: #bfe2dc;
    --aqua-soft: #cfe3e0;
    --grain-grey: #c7c8c8;
    --grain-light: #dcdcdc;
    --ink: #111111;
    --ink-soft: #3a4a4a;
    --silver: #e6e7e8;
    --silver-edge: #9a9c9e;
  }
  html, body {
    margin: 0;
    width: 1200px;
    height: 1200px;
    overflow: hidden;
    background: var(--page-bg);
  }
  .canvas {
    position: relative;
    width: 1200px;
    height: 1200px;
  }
  .label {
    position: absolute;
    left: 290px;
    top: 225px;
    width: 620px;
    height: 750px;
    box-sizing: border-box;
    border: 14px solid var(--label-border);
    border-radius: 14px;
    background: linear-gradient(to bottom, var(--aqua) 0%, var(--aqua-soft) 35%, var(--grain-light) 62%, var(--grain-grey) 100%);
    box-shadow: 0 2px 10px rgba(0,0,0,0.08);
    overflow: hidden;
  }
  .woodgrain {
    position: absolute;
    left: 0; right: 0; bottom: 0;
    height: 58%;
    background: linear-gradient(to bottom, rgba(220,220,220,0) 0%, rgba(205,206,206,0.7) 40%, var(--grain-grey) 100%);
  }
  .tagline {
    position: relative;
    margin: 28px 0 0;
    text-align: center;
    font-family: "Dancing Script", cursive;
    font-weight: 500;
    font-size: 32px;
    color: var(--ink-soft);
  }
  .brand-mark {
    position: relative;
    margin: 18px auto 0;
    width: 282px;
    height: 282px;
    border-radius: 50%;
    background: var(--silver);
    border: 3px solid var(--silver-edge);
    box-sizing: border-box;
    display: flex;
    align-items: center;
    justify-content: center;
  }
  .brand-name {
    font-family: "PT Sans", sans-serif;
    font-weight: 400;
    font-size: 46px;
    color: var(--ink);
    letter-spacing: 2px;
  }
  .product-title {
    position: relative;
    margin: 44px 0 0;
    text-align: center;
    font-family: "PT Sans", sans-serif;
    font-weight: 400;
    font-size: 54px;
    color: var(--ink);
  }
  .product-desc {
    position: relative;
    margin: 14px 0 0;
    text-align: center;
    font-family: "Tinos", serif;
    font-size: 25px;
    line-height: 1.45;
    color: var(--ink);
  }
  .volume {
    position: absolute;
    left: 0; right: 0;
    bottom: 14px;
    text-align: center;
    font-family: "Tinos", serif;
    font-style: italic;
    font-weight: 700;
    font-size: 17px;
    color: var(--ink);
  }
</style>
</head>
<body>
<main class="canvas">
  <section class="label">
    <div class="woodgrain" role="img" aria-label="Soft grey woodgrain texture"></div>
    <p class="tagline">Formulated by a Naturopath</p>
    <div class="brand-mark">
      <span class="brand-name">velmurine</span>
    </div>
    <h1 class="product-title">Anti-aging Therapy</h1>
    <p class="product-desc">Organic Facial Oil with CoEnzyme Q10<br>Rosehip Seed Oil</p>
    <p class="volume">100ml e3.38fl.oz.</p>
  </section>
</main>
</body>
</html>
```